Brightwren Farming

We need a logo design for a new company based in Kelowna, BC. We grow market garden vegetables for sale at market and in a CSA program. We try to only use hand tools for all aspects of cultivating, seeding, weeding, harvesting and distributing. For this reason we consider ourselves very low impact on the environment.

We would like blues and green in the design with an earthy, natural feel

Target Market(s)

Environmentally aware, health conscience

Industry/Entity Type

Farming

Requirements
Must have
• Foot prints with section for contact details all on the one side
Should not have
• Dark, black colours or anything that looks unnatural

```html
<!DOCTYPE html>
<html lang="en">
<head>
<meta charset="utf-8">
<title>Brightwren Farming – Business Card</title>
<link href="https://fonts.googleapis.com/css2?family=Lato:wght@400;700&family=Raleway:wght@600;700&display=swap" rel="stylesheet">
<style>
  :root {
    --stage: #4a4a4a;
    --slate: #44565a;
    --leaf: #7cc242;
    --leaf-mid: #5f9a4c;
    --paper: #ffffff;
    --rule: #c9d0d1;
  }
  * { margin: 0; padding: 0; box-sizing: border-box; }
  html, body { width: 900px; height: 1200px; overflow: hidden; }
  body { background: var(--stage); position: relative; font-family: "Lato", sans-serif; }

  .card {
    position: absolute; left: 110px; width: 673px; height: 396px;
    border-radius: 22px; overflow: hidden;
  }
  .card--front {
    top: 173px;
    background: linear-gradient(180deg, var(--slate) 0%, var(--leaf-mid) 55%, var(--leaf) 100%);
  }
  .card--back { top: 629px; background: var(--paper); }

  .brand { position: absolute; display: flex; flex-direction: column; align-items: center; font-family: "Lato", sans-serif; font-weight: 700; }
  .brand__dot { width: 64px; height: 64px; border-radius: 50%; margin-bottom: 22px; }
  .brand__name { font-size: 46px; line-height: 1.05; text-align: center; }

  .card--front .brand { left: 0; right: 0; top: 72px; color: var(--paper); }
  .card--front .brand__dot { background: var(--paper); }

  .card--back .brand { left: 40px; width: 290px; top: 62px; color: var(--slate); }
  .card--back .brand__dot { background: var(--leaf); }
  .card--back .brand__name { font-size: 40px; }

  .divider { position: absolute; left: 346px; top: 76px; width: 1px; height: 210px; background: var(--rule); }

  .contact { position: absolute; left: 385px; top: 101px; }
  .contact__name { font-family: "Raleway", sans-serif; font-weight: 700; font-size: 22px; color: var(--slate); letter-spacing: 0.5px; }
  .contact__role { font-family: "Raleway", sans-serif; font-weight: 600; font-size: 13.5px; color: var(--leaf); margin-top: 2px; letter-spacing: 0.3px; }
  .contact__list { list-style: none; margin-top: 19px; }
  .contact__item { display: flex; align-items: center; height: 24px; font-size: 16.5px; color: var(--slate); }
  .contact__icon { width: 14px; height: 14px; margin: 0 13px 0 1px; fill: var(--leaf); }

  .wave { position: absolute; left: 0; bottom: 0; width: 673px; height: 80px; }
</style>
</head>
<body>

<section class="card card--front" aria-label="Card front">
  <div class="brand">
    <span class="brand__dot"></span>
    <span class="brand__name">Brightwren<br>Farming</span>
  </div>
</section>

<section class="card card--back" aria-label="Card back">
  <div class="brand">
    <span class="brand__dot"></span>
    <span class="brand__name">Brightwren<br>Farming</span>
  </div>

  <div class="divider"></div>

  <div class="contact">
    <h1 class="contact__name">OWEN HARLOW</h1>
    <p class="contact__role">MANAGING DIRECTOR</p>
    <ul class="contact__list">
      <li class="contact__item">
        <svg class="contact__icon" viewBox="0 0 14 14"><path d="M2 1h10v12H2z M3.5 2.5v7h7v-7z M6 10.5h2v1.2H6z" fill-rule="evenodd"/></svg>
        0400-555-218
      </li>
      <li class="contact__item">
        <svg class="contact__icon" viewBox="0 0 14 14"><path d="M3 1l2.5 2.7-1.4 1.8c.9 1.9 2.4 3.4 4.3 4.3l1.8-1.4L13 11l-1.6 2C6 12.6 1.4 8 1 2.6z"/></svg>
        0700-555-412
      </li>
      <li class="contact__item">
        <svg class="contact__icon" viewBox="0 0 14 14"><path d="M1 2.5h12v9H1z M2.2 3.5L7 7.3l4.8-3.8z" fill-rule="evenodd"/></svg>
        owenharlow@brightwren.com
      </li>
      <li class="contact__item">
        <svg class="contact__icon" viewBox="0 0 14 14" fill="none" stroke="#7cc242" stroke-width="1.2"><circle cx="7" cy="7" r="5.8"/><ellipse cx="7" cy="7" rx="2.6" ry="5.8"/><path d="M1.2 7h11.6M2 4h10M2 10h10"/></svg>
        www.owenharlow.com
      </li>
    </ul>
  </div>

  <svg class="wave" viewBox="0 0 673 80" preserveAspectRatio="none" aria-hidden="true">
    <path d="M0 2 C90 0 200 4 300 14 L300 17 C200 10 90 10 0 14 Z" fill="#7cc242"/>
    <path d="M360 36 C480 36 590 22 673 0 L673 14 C590 32 480 40 360 36 Z" fill="#7cc242"/>
    <path d="M0 20 C120 16 240 24 360 42 C480 48 590 36 673 20 L673 80 L0 80 Z" fill="#44565a"/>
  </svg>
</section>

</body>
</html>
```